Christmas / Holiday themed front and back wine label set
Warm Mulled Wine / hot spiced wine
We need a hot spice wine label that screams Christmas / Thanksgiving / the holidays. Need a front and back label set. Label needs to be obvious holiday themed so retailers can display / sell for the Christmas holiday season. Wine is a green, 750ml standard wine bottle, with a dravoke screw top seal. We can pick standard colors for the screw cap to match your label design.
Beverages
Adults 21 to 70 years old. A hot spiced wine, served warm, about the temperature of hot chocolate at holiday parties and family gatherings. It also can be given as a "Christmas gift" to friends, family and holiday workers.
Front label 3 1/2" wide by 4 1/2" tall max size. Back label 3" wide by 4 1/2" tall max size. Some legal text will need to be added after the winning design is selected for the back label. The following text should be incorporated on either the front or back label "Warm Mulled Wine, a light table wine with honey, unfermented cider lemon juices and spices." Also "SERVE WARM but do not boil" Also "Alcohol 9% by volume". On the back label will need to add a UPC number too along with the "GOVERNMENT WARNING"

```html
<!DOCTYPE html>
<html lang="en">
<head>
<meta charset="utf-8">
<title>Warm Mulled Wine – Holiday Label Set</title>
<link href="https://fonts.googleapis.com/css2?family=IM+Fell+English+SC&family=Libre+Baskerville:wght@400;700&display=swap" rel="stylesheet">
<style>
  :root {
    --backdrop: #f1ebe3;
    --label-white: #ffffff;
    --navy: #1b2a5e;
    --holly-red: #d51f2b;
    --wine-red: #b3121c;
    --wine-deep: #6e0a10;
    --pine-green: #1e8a3c;
    --cream: #fbf6ee;
    --ink-grey: #6b6b6b;
    --antler-brown: #8a5a36;
  }
  * { margin: 0; padding: 0; box-sizing: border-box; }
  html, body { width: 1200px; height: 749px; overflow: hidden; background: var(--backdrop); }
  .canvas { position: relative; width: 1200px; height: 749px; }

  .label { position: absolute; top: 82px; width: 470px; height: 580px; }
  .label--front { left: 100px; }
  .label--back { left: 632px; }
  .label__frame { position: absolute; inset: 0; width: 470px; height: 580px; }

  .label p, .label h1, .label h2 { white-space: nowrap; }

  .artwork { position: absolute; }
  .snowfall {
    left: 19px; top: 19px; width: 432px; height: 390px;
    border-radius: 16px 16px 0 0;
    background: radial-gradient(ellipse at 50% 0%, rgba(255,255,255,.22) 0%, rgba(255,255,255,.08) 45%, rgba(255,255,255,0) 75%);
  }
  .mascot {
    left: 140px; top: 268px; width: 192px; height: 142px;
    background: radial-gradient(ellipse at 50% 70%, #a06a40 0%, var(--antler-brown) 55%, #5e3a22 100%);
    border-radius: 90px 90px 0 0;
  }

  .serve-warm {
    position: absolute; left: 0; right: 0; text-align: center;
    font-family: "Libre Baskerville", Georgia, serif;
    letter-spacing: 5px; font-size: 16px; line-height: 1;
  }
  .serve-warm small { font-size: 6px; letter-spacing: 0; vertical-align: super; margin-left: 2px; }

  /* Front label */
  .front__lettering {
    left: 159px; top: 81px; width: 161px; height: 161px;
    background: linear-gradient(180deg, #ffffff 0%, #f3d6d8 100%);
    border-radius: 22px;
  }
  .front .serve-warm { top: 422px; color: var(--ink-grey); }
  .front__name {
    position: absolute; left: 0; right: 0; top: 450px; text-align: center;
    font-family: "Libre Baskerville", Georgia, serif; font-weight: 700;
    color: var(--holly-red); font-size: 36px; line-height: 1.1;
  }
  .front__ingredients {
    position: absolute; left: 0; right: 0; top: 500px; text-align: center;
    font-family: "Libre Baskerville", Georgia, serif; color: var(--holly-red); font-size: 11px;
  }
  .front__volume {
    position: absolute; right: 44px; top: 536px;
    font-family: "Libre Baskerville", Georgia, serif; color: var(--holly-red); font-size: 16px;
  }
  .front__abv {
    position: absolute; left: 442px; top: 416px; transform: rotate(90deg); transform-origin: left top;
    font-family: "Libre Baskerville", Georgia, serif; color: var(--holly-red); font-size: 13px;
  }

  /* Back label */
  .back__title {
    position: absolute; left: 0; right: 0; top: 124px; text-align: center;
    font-family: "IM Fell English SC", Georgia, serif; font-weight: 400;
    color: var(--label-white); font-size: 42px; line-height: 1;
  }
  .back__subtitle {
    position: absolute; left: 0; right: 0; top: 212px; text-align: center;
    font-family: "Libre Baskerville", Georgia, serif; color: var(--label-white); font-size: 28px; line-height: 1;
  }
  .back__ingredients {
    position: absolute; left: 0; right: 0; top: 420px; text-align: center;
    font-family: "Libre Baskerville", Georgia, serif; color: var(--holly-red); font-size: 14px;
  }
  .back .serve-warm { top: 458px; color: var(--holly-red); }
  .back__row {
    position: absolute; left: 36px; right: 36px; top: 488px;
    display: flex; justify-content: space-between; align-items: center;
    font-family: "Libre Baskerville", Georgia, serif; color: var(--holly-red); font-size: 18px;
  }
  .back__emblem { width: 26px; height: 34px; background: var(--holly-red); border-radius: 5px; }
  .back__tagline {
    position: absolute; left: 0; right: 0; top: 540px; text-align: center;
    font-family: "Libre Baskerville", Georgia, serif; color: var(--holly-red); font-size: 9px;
  }
</style>
</head>
<body>
<main class="canvas">

  <section class="label label--front front">
    <svg class="label__frame" viewBox="0 0 470 580" aria-hidden="true">
      <defs>
        <clipPath id="front-inner">
          <path d="M36 18 H434 A18 18 0 0 0 452 36 V544 A18 18 0 0 0 434 562 H36 A18 18 0 0 0 18 544 V36 A18 18 0 0 0 36 18 Z"/>
        </clipPath>
      </defs>
      <path d="M29 3 H441 A26 26 0 0 0 467 29 V551 A26 26 0 0 0 441 577 H29 A26 26 0 0 0 3 551 V29 A26 26 0 0 0 29 3 Z"
            fill="var(--label-white)" stroke="var(--holly-red)" stroke-width="5"/>
      <g clip-path="url(#front-inner)">
        <rect x="0" y="0" width="470" height="580" fill="var(--label-white)"/>
        <rect x="0" y="0" width="470" height="410" fill="var(--navy)"/>
      </g>
      <path d="M36 18 H434 A18 18 0 0 0 452 36 V544 A18 18 0 0 0 434 562 H36 A18 18 0 0 0 18 544 V36 A18 18 0 0 0 36 18 Z"
            fill="none" stroke="var(--holly-red)" stroke-width="2"/>
    </svg>
    <div class="artwork snowfall" role="img" aria-label="White snowflakes falling across the night sky"></div>
    <div class="artwork front__lettering" role="img" aria-label="Hand lettered title: Warm Mulled Wine, red letters on white"></div>
    <div class="artwork mascot" role="img" aria-label="Cartoon reindeer in a Santa hat peeking over the edge"></div>
    <p class="serve-warm">SERVE WARM<small>do not boil</small></p>
    <h1 class="front__name">Holly Glow</h1>
    <p class="front__ingredients">Unfermented Cider Lemon Juices And Spices</p>
    <p class="front__volume">750ml</p>
    <p class="front__abv">Alcohol 9%</p>
  </section>

  <section class="label label--back back">
    <svg class="label__frame" viewBox="0 0 470 580" aria-hidden="true">
      <defs>
        <radialGradient id="wine-glow" cx="50%" cy="30%" r="75%">
          <stop offset="0" stop-color="#d4232d"/>
          <stop offset="0.6" stop-color="var(--wine-red)"/>
          <stop offset="1" stop-color="var(--wine-deep)"/>
        </radialGradient>
        <clipPath id="back-inner">
          <path d="M36 18 H434 A18 18 0 0 0 452 36 V544 A18 18 0 0 0 434 562 H36 A18 18 0 0 0 18 544 V36 A18 18 0 0 0 36 18 Z"/>
        </clipPath>
      </defs>
      <path d="M29 3 H441 A26 26 0 0 0 467 29 V551 A26 26 0 0 0 441 577 H29 A26 26 0 0 0 3 551 V29 A26 26 0 0 0 29 3 Z"
            fill="var(--label-white)" stroke="var(--pine-green)" stroke-width="5"/>
      <g clip-path="url(#back-inner)">
        <rect x="0" y="0" width="470" height="580" fill="var(--cream)"/>
        <rect x="0" y="0" width="470" height="410" fill="url(#wine-glow)"/>
        <rect x="0" y="408" width="470" height="3" fill="var(--holly-red)"/>
      </g>
      <path d="M36 18 H434 A18 18 0 0 0 452 36 V544 A18 18 0 0 0 434 562 H36 A18 18 0 0 0 18 544 V36 A18 18 0 0 0 36 18 Z"
            fill="none" stroke="var(--holly-red)" stroke-width="2"/>
    </svg>
    <div class="artwork snowfall" role="img" aria-label="White snowflakes falling across the red sky"></div>
    <h2 class="back__title">Hot Spiced Wine</h2>
    <p class="back__subtitle">Merry Mug</p>
    <div class="artwork mascot" role="img" aria-label="Cartoon reindeer in a Santa hat peeking over the edge"></div>
    <p class="back__ingredients">Unfermented Cider Lemon Juices And Spices</p>
    <p class="serve-warm">SERVE WARM<small>do not boil</small></p>
    <div class="back__row">
      <span>750ml</span>
      <span class="back__emblem" role="img" aria-label="Small stag head emblem"></span>
      <span>Alcohol 9%</span>
    </div>
    <p class="back__tagline">Warm Mulled Wine, a light table wine with honey,</p>
  </section>

</main>
</body>
</html>
```